Professional/Sleek card design for athletic apparel brand

Athletic apparel brand. Mainly focused on lifting weights/gym workouts. Logo and brand are already created. Must use brand logo and name. Creativity is welcome. Looking for a clean, modern, and sexy design.

```html
<!DOCTYPE html>
<html lang="en">
<head>
<meta charset="utf-8">
<title>Iron and Grit — Business Card</title>
<link href="https://fonts.googleapis.com/css2?family=Michroma&family=Exo+2:wght@400;500;700&display=swap" rel="stylesheet">
<style>
  :root {
    --backdrop: #8e8e8e;
    --card-dark: #1e1e1e;
    --card-light: #ececec;
    --gold: #b8934a;
    --ink: #3a3a3a;
    --ink-soft: #555555;
    --rule: #9a9a9a;
  }
  * { margin: 0; padding: 0; box-sizing: border-box; }
  html, body {
    width: 1200px;
    height: 1200px;
    overflow: hidden;
    background: var(--backdrop);
  }
  .canvas { position: relative; width: 1200px; height: 1200px; }

  .card {
    position: absolute;
    width: 746px;
    height: 435px;
    border-radius: 26px;
    overflow: hidden;
  }
  .card--front { left: 215px; top: 128px; background: var(--card-dark); }
  .card--back  { left: 218px; top: 604px; background: var(--card-light); }

  .wordmark {
    position: absolute;
    left: 0;
    right: 0;
    text-align: center;
    font-family: "Michroma", sans-serif;
    font-weight: 400;
    color: var(--gold);
    white-space: nowrap;
  }
  .card--front .wordmark {
    top: 252px;
    font-size: 24px;
    letter-spacing: 1.15em;
    padding-left: 1.15em;
  }
  .card--back .wordmark {
    top: 114px;
    font-size: 14px;
    letter-spacing: 1.15em;
    padding-left: 1.15em;
  }

  .holder {
    position: absolute;
    right: calc(746px - 342px);
    top: 244px;
    text-align: right;
    font-family: "Exo 2", sans-serif;
  }
  .holder__name {
    font-weight: 700;
    font-size: 18px;
    letter-spacing: 0.06em;
    color: var(--ink);
    text-transform: uppercase;
  }
  .holder__title {
    margin-top: 2px;
    font-weight: 500;
    font-size: 13px;
    letter-spacing: 0.16em;
    color: var(--ink-soft);
    text-transform: uppercase;
  }

  .divider {
    position: absolute;
    left: 363px;
    top: 206px;
    width: 1px;
    height: 134px;
    background: var(--rule);
  }

  .contact {
    position: absolute;
    left: 382px;
    top: 206px;
    font-family: "Exo 2", sans-serif;
    font-size: 17px;
    line-height: 19px;
    letter-spacing: 0.02em;
    color: var(--ink);
  }
  .contact__address { margin-bottom: 14px; }
  .contact__row {
    display: flex;
    align-items: center;
    height: 24px;
  }
  .contact__icon {
    width: 16px;
    height: 16px;
    margin-right: 8px;
    flex: none;
  }
  .contact__row--email { font-size: 16px; }
</style>
</head>
<body>
<main class="canvas">
  <section class="card card--front" aria-label="Card front">
    <div class="wordmark">IRON AND GRIT</div>
  </section>

  <section class="card card--back" aria-label="Card back">
    <div class="wordmark">IRON AND GRIT</div>

    <div class="holder">
      <p class="holder__name">Marcus Delvane</p>
      <p class="holder__title">Founder &amp; CEO</p>
    </div>

    <div class="divider"></div>

    <div class="contact">
      <p class="contact__address">4820 E Summit Ave. Ste. 210<br>Mesa, AZ 85201</p>

      <p class="contact__row">
        <svg class="contact__icon" viewBox="0 0 16 16" fill="none" stroke="#3a3a3a" stroke-width="1.2" aria-hidden="true">
          <path d="M3.5 1.5l2.5 3-1.6 1.6c.8 1.9 2.4 3.5 4.3 4.3L10.3 8.8l3 2.5-1.4 2.6c-5.5-.4-9.8-4.7-10.2-10.2z"/>
        </svg>
        1 (800) 555-0142 Ext. 314
      </p>
      <p class="contact__row">
        <svg class="contact__icon" viewBox="0 0 16 16" fill="none" stroke="#3a3a3a" stroke-width="1.2" aria-hidden="true">
          <rect x="4" y="1" width="8" height="14" rx="1.5"/>
          <line x1="7" y1="12.5" x2="9" y2="12.5"/>
        </svg>
        (480) 555-0187
      </p>
      <p class="contact__row contact__row--email">
        <svg class="contact__icon" viewBox="0 0 16 16" fill="none" stroke="#3a3a3a" stroke-width="1.2" aria-hidden="true">
          <rect x="1.5" y="3.5" width="13" height="9"/>
          <path d="M1.5 3.5L8 9l6.5-5.5"/>
        </svg>
        mdelvane@ironandgritapparel.com
      </p>
    </div>
  </section>
</main>
</body>
</html>
```